Simple and elegant Wallsaver Packaging needed for our new product

We are looking for a packaging for our new wallsaver product, which primary purpose is to protect damages to the wall. It prevents drilling holes into the wall.

Packaging file can be found - https://files.plorvex.net/open?id=7Kzq2RTmwobNXvLcaHyuPEsjDfG

The company name is Dornaby and i have attached pictures of the product and the company logo that we would like on the packaging.

Examples of packaging we like in terms of packaging are tavsen packaging and frome & lattis packaging.

Copies of instructions to set up the product are on the 5th picture on this link - https://www.shopvarro.co.uk/d/kpt/Belvo-Pressure-Guard-Surface-Gates-Curtain-Tension-Mounted/Z73K4WQM2J.
Updates

All,I have updated the brief and add more info about the packaging so please have another look.I look forward to receiving your designs and giving feedback.Thanks Added Thursday, January 12, 2017

Hi All, We still awaiting for more entries before making our final decision. Happy to assist if anyone has further queries. Thanks

One more day left so please submit your designs. I will be giving feedback shortly on the designs received so far. A few designers have asked for me to extend the competition so they have time to submit, so i may do this. Regards Tesk

Reason: Hi, I am extending the deadline so designers can incorporate the feedback i am going to give. So i can get the best possible design possible. Thanks

Target Market(s)

Homeowners

Industry/Entity Type

Home Improvement

Requirements
Must have
• Logo, Instructions to use
Nice to have
• Pictures of product

```html
<!DOCTYPE html>
<html lang="en">
<head>
<meta charset="utf-8">
<title>Dornaby Pressure Gate Wall Saver – Packaging Panels</title>
<link href="https://fonts.googleapis.com/css2?family=Montserrat:wght@500;600;700&family=Roboto:wght@400;500&display=swap" rel="stylesheet">
<style>
  :root {
    --canvas: #b3b3b3;
    --paper: #ffffff;
    --charcoal: #2b2c30;
    --slate: #4a4a4d;
    --brand-red: #d6343f;
    --ink: #1f1f22;
    --text-light: #ffffff;
  }
  * { box-sizing: border-box; margin: 0; padding: 0; }
  html, body { width: 1200px; height: 900px; overflow: hidden; }
  body {
    background: var(--canvas);
    font-family: "Montserrat", sans-serif;
    position: relative;
  }
  .panel {
    position: absolute;
    overflow: hidden;
    box-shadow: 0 6px 18px rgba(0,0,0,0.18);
  }
  .panel svg { display: block; width: 100%; height: 100%; }
  .panel--lid   { left: 40px;  top: 50px;  width: 720px; height: 380px; }
  .panel--front { left: 40px;  top: 450px; width: 720px; height: 380px; }
  .panel--uses  { left: 780px; top: 50px;  width: 380px; height: 380px; background: var(--slate); }
  .panel--features { left: 780px; top: 450px; width: 380px; height: 380px; background: var(--slate); }

  .brand-name { font-family: "Montserrat", sans-serif; font-weight: 500; fill: var(--ink); letter-spacing: 3px; }
  .product-title { font-family: "Montserrat", sans-serif; font-weight: 600; fill: var(--text-light); }
  .pack-count { font-family: "Montserrat", sans-serif; fill: var(--text-light); }
  .banner-text { font-family: "Montserrat", sans-serif; font-weight: 700; fill: var(--text-light); letter-spacing: 1px; }
  .lid-points { font-family: "Roboto", sans-serif; font-size: 15px; fill: var(--text-light); }

  .features-stripe { position: absolute; inset: 0; }
  .feature-list {
    position: absolute;
    left: 30px; right: 26px; top: 34px;
    list-style: none;
    font-family: "Roboto", sans-serif;
    font-size: 16px;
    line-height: 1.35;
    color: var(--text-light);
  }
  .feature-list li { position: relative; padding-left: 22px; margin-bottom: 18px; }
  .feature-list li::before {
    content: ""; position: absolute; left: 0; top: 6px;
    width: 9px; height: 9px; border-radius: 50%; background: var(--text-light);
  }

  .uses-grid {
    position: absolute; inset: 24px;
    display: grid; grid-template-columns: 1fr 1fr; gap: 16px;
  }
  .use-card { display: flex; flex-direction: column; gap: 10px; }
  .use-caption {
    font-family: "Roboto", sans-serif; font-size: 13px; line-height: 1.3;
    color: var(--text-light); min-height: 36px;
  }
  .use-photo { flex: 1; border-radius: 2px; }
  .use-photo--gate { background: linear-gradient(160deg, #d9c3a0 0%, #b89a72 45%, #efece6 100%); }
  .use-photo--curtain { background: linear-gradient(160deg, #f4f4f2 0%, #dfe3e6 55%, #b9c1c7 100%); }
</style>
</head>
<body>

<section class="panel panel--lid">
  <svg viewBox="0 0 720 380" aria-label="Lid panel">
    <defs>
      <linearGradient id="lidDark" x1="0" y1="0" x2="1" y2="1">
        <stop offset="0" stop-color="#55565a"/>
        <stop offset="1" stop-color="#2b2c30"/>
      </linearGradient>
    </defs>
    <rect width="720" height="380" fill="var(--paper)"/>
    <polygon points="430,0 720,0 720,380 560,380" fill="url(#lidDark)"/>
    <polygon points="300,0 720,0 720,70 330,70" fill="var(--brand-red)"/>
    <polygon points="270,0 292,0 322,70 300,70" fill="var(--charcoal)"/>
    <text class="banner-text" x="700" y="43" font-size="20" text-anchor="end">PRESSURE GATE WALL SAVER</text>
    <circle cx="60" cy="150" r="10" fill="var(--brand-red)"/>
    <text class="brand-name" x="84" y="168" font-size="50">DORNABY</text>
    <polygon points="0,300 420,230 440,255 0,335" fill="var(--brand-red)"/>
    <g class="lid-points">
      <circle cx="522" cy="124" r="4" fill="#fff"/><text x="534" y="129">Easy Fast Installation</text>
      <circle cx="522" cy="156" r="4" fill="#fff"/><text x="534" y="161">No Tools Required</text>
      <circle cx="522" cy="188" r="4" fill="#fff"/><text x="534" y="193">Used for Pressure</text>
      <text x="534" y="213">Mounted Gate</text>
    </g>
  </svg>
</section>

<section class="panel panel--front">
  <svg viewBox="0 0 720 380" aria-label="Front panel">
    <defs>
      <linearGradient id="frontDark" x1="0" y1="0" x2="1" y2="0">
        <stop offset="0" stop-color="#1f2024"/>
        <stop offset="1" stop-color="#6a6a6d"/>
      </linearGradient>
      <linearGradient id="baseDark" x1="0" y1="0" x2="1" y2="0">
        <stop offset="0" stop-color="#3a3b3f"/>
        <stop offset="1" stop-color="#505053"/>
      </linearGradient>
      <radialGradient id="padTone" cx="0.45" cy="0.45" r="0.6">
        <stop offset="0" stop-color="#f2f2f2"/>
        <stop offset="1" stop-color="#b9b9b9"/>
      </radialGradient>
    </defs>
    <rect width="720" height="380" fill="var(--paper)"/>
    <polygon points="0,20 520,300 0,380" fill="url(#frontDark)"/>
    <polygon points="0,380 720,190 720,380" fill="url(#baseDark)"/>
    <polygon points="150,340 720,150 720,200 190,372" fill="var(--brand-red)"/>
    <polygon points="0,250 230,228 230,244 0,268" fill="var(--brand-red)"/>
    <text class="product-title" x="24" y="172" font-size="26">Pressure Gate</text>
    <text class="product-title" x="24" y="204" font-size="26">Wall Saver</text>
    <circle cx="268" cy="80" r="10" fill="var(--brand-red)"/>
    <text class="brand-name" x="292" y="98" font-size="54">DORNABY</text>
    <ellipse role="img" aria-label="Product photo: white round wall saver pad with grey ribbed rubber backing" cx="560" cy="220" rx="100" ry="88" fill="url(#padTone)"/>
    <text class="pack-count" x="590" y="352"><tspan font-size="40" font-weight="700">4</tspan><tspan font-size="30" font-weight="500" dx="10">Pack</tspan></text>
  </svg>
</section>

<section class="panel panel--uses">
  <div class="uses-grid">
    <div class="use-card">
      <p class="use-caption">Save your wall &amp; makes the gate more stable</p>
      <div class="use-photo use-photo--gate" role="img" aria-label="Photo: wall saver pad fitted between a pressure gate and a wall"></div>
    </div>
    <div class="use-card">
      <p class="use-caption">For Shower curtain with tension mounted rod.</p>
      <div class="use-photo use-photo--curtain" role="img" aria-label="Photo: wall saver pad on the end of a tension shower curtain rod"></div>
    </div>
  </div>
</section>

<section class="panel panel--features">
  <svg class="features-stripe" viewBox="0 0 380 380" preserveAspectRatio="none" aria-hidden="true">
    <polygon points="0,360 380,250 380,290 0,380" fill="var(--brand-red)"/>
  </svg>
  <ul class="feature-list">
    <li>Easy Fast Installation, No Tools Required, Used for Pressure Mounted Gate.</li>
    <li>Oversized Pad Protects Walls Better, Large Surface Area and Rubber Backing Pad with Little Suckers Make For More Stable Installation And More Security.</li>
    <li>Use on Top Spindles Only - Not Needed on Doorways With Doors Installed.</li>
    <li>Thick Pad Equalizes Distance From The Top to Bottom of Gate.</li>
  </ul>
</section>

</body>
</html>
```